Business Card Design Project

i have the logo designed.
I require designs for the managing director and the general manager.
we need space for email, and a mobile number.
any other cool stuff/design you guys just let me see what you got.
The managing director card could be black, minimalist, and the cards for the rest of the company could be using the green logo.
it has to impress. transportation market is fragmented, we want to appear professional and sophisticated.
Md: Tariq walid hussain
General manager: nabil hussain
Target Market(s)
clients: procurement heads of contracting companies
Industry/Entity Type
Business

```html
<!DOCTYPE html>
<html lang="en">
<head>
<meta charset="utf-8">
<title>Fleetmark Business Card</title>
<link rel="stylesheet" href="https://fonts.googleapis.com/css2?family=Saira:wght@400;600&display=swap">
<style>
  :root {
    --backdrop: #3b2f28;
    --card: #ffffff;
    --brand-green: #1f8a3c;
    --name-green: #34a24f;
    --ink-grey: #8c8c8c;
    --shadow: rgba(0, 0, 0, 0.45);
  }
  * { margin: 0; padding: 0; box-sizing: border-box; }
  html, body {
    width: 1200px;
    height: 469px;
    overflow: hidden;
    background: var(--backdrop);
    font-family: "Saira", "Helvetica Neue", Arial, sans-serif;
  }
  .stage {
    position: relative;
    width: 1200px;
    height: 469px;
  }
  .card {
    position: absolute;
    top: 102px;
    width: 464px;
    height: 265px;
    background: var(--card);
    box-shadow: 0 4px 10px var(--shadow);
  }
  .card--front { left: 106px; }
  .card--back { left: 598px; }

  .holder-name {
    position: absolute;
    top: 115px;
    left: 0;
    width: 100%;
    text-align: center;
    font-size: 19px;
    font-weight: 400;
    letter-spacing: 2px;
    color: var(--name-green);
    text-transform: uppercase;
  }
  .holder-phone {
    position: absolute;
    top: 143px;
    left: 0;
    width: 100%;
    text-align: center;
    font-size: 13px;
    letter-spacing: 0.5px;
    color: var(--ink-grey);
  }

  .brand-name {
    position: absolute;
    top: 112px;
    right: 102px;
    font-size: 31px;
    font-weight: 600;
    line-height: 1;
    color: var(--brand-green);
  }
  .brand-web,
  .brand-mail {
    position: absolute;
    right: 104px;
    font-size: 12.5px;
    color: var(--ink-grey);
    text-align: right;
  }
  .brand-web { top: 156px; letter-spacing: 3px; }
  .brand-mail { top: 175px; letter-spacing: 1px; }
</style>
</head>
<body>
  <main class="stage">
    <section class="card card--front" aria-label="Card front">
      <p class="holder-name">Tariq Walid Hussain</p>
      <p class="holder-phone">Phone: 098.765.4321</p>
    </section>
    <section class="card card--back" aria-label="Card back">
      <p class="brand-name">Fleetmark</p>
      <p class="brand-web">www.fleetmark.com</p>
      <p class="brand-mail">name@fleetmark.com</p>
    </section>
  </main>
</body>
</html>
```